Business Card Design Project

We're an orthopaedic office, and our colors are blue white and balck. Dealing with physicians and healthcare execs, I'd like this card to have a classy, yet overpowering wow factor.

Here are a couple of cards I like that are close to what I'm looking for:
http://www.pixelbazaro.com/design/392047
http://www.pixelbazaro.com/design/286390

Industry/Entity Type

Healthcare

```html
<!DOCTYPE html>
<html lang="en">
<head>
<meta charset="utf-8">
<title>Keystone Orthopaedic – Business Card</title>
<link rel="stylesheet" href="https://fonts.googleapis.com/css2?family=Ubuntu:wght@400;500;700&display=swap">
<style>
  :root {
    --brand-blue: #1f3f9c;
    --brand-blue-soft: #e9edf7;
    --ink: #2b2b2b;
    --paper: #ffffff;
    --backdrop: #ececec;
  }
  * { margin: 0; padding: 0; box-sizing: border-box; }
  html, body { width: 1200px; height: 1000px; overflow: hidden; }
  body {
    background: var(--backdrop);
    font-family: "Ubuntu", sans-serif;
    display: flex;
    flex-direction: column;
    align-items: center;
    justify-content: center;
    gap: 70px;
  }
  .card {
    position: relative;
    width: 600px;
    height: 343px;
    border-radius: 4px;
    box-shadow: 0 6px 18px rgba(0,0,0,0.18);
    overflow: hidden;
  }

  /* Front */
  .card--front { background: var(--paper); }
  .card__tab {
    position: absolute; top: 0; right: 0;
    width: 26px; height: 44px;
    background: var(--brand-blue);
  }
  .holder {
    position: absolute; top: 40px; right: 52px;
    text-align: right; color: var(--brand-blue);
  }
  .holder__name { font-size: 24px; font-weight: 700; }
  .holder__title { font-size: 19px; font-weight: 400; margin-top: 2px; }

  .brand {
    position: absolute; left: 40px; top: 150px;
    display: flex; align-items: center; gap: 12px;
    color: var(--brand-blue);
  }
  .brand__dot {
    width: 22px; height: 22px; border-radius: 50%;
    background: var(--brand-blue);
  }
  .brand__name { font-size: 30px; font-weight: 500; line-height: 1; letter-spacing: 0.5px; }
  .brand__sub { font-size: 13px; font-weight: 400; line-height: 1.2; margin-top: 3px; color: var(--ink); }

  .contact {
    position: absolute; left: 40px; bottom: 34px;
    list-style: none; color: var(--ink);
    font-size: 15px;
  }
  .contact__item { display: flex; align-items: center; gap: 12px; height: 26px; }
  .contact__icon {
    width: 16px; height: 16px; border-radius: 50%;
    border: 1.2px solid var(--brand-blue);
    display: flex; align-items: center; justify-content: center;
  }
  .contact__icon svg { width: 9px; height: 9px; fill: var(--brand-blue); }

  /* Back */
  .card--back {
    background: var(--brand-blue);
    display: flex; align-items: center; justify-content: center;
  }
  .card--back .brand {
    position: static; color: var(--paper); gap: 16px;
  }
  .card--back .brand__dot { background: var(--paper); width: 30px; height: 30px; }
  .card--back .brand__name { font-size: 42px; }
  .card--back .brand__sub { color: var(--paper); font-size: 17px; }
</style>
</head>
<body>

<section class="card card--front">
  <div class="card__tab"></div>
  <div class="holder">
    <p class="holder__name">Graham Whitfield</p>
    <p class="holder__title">CEO</p>
  </div>

  <div class="brand">
    <span class="brand__dot"></span>
    <div>
      <p class="brand__name">KEYSTONE</p>
      <p class="brand__sub">Orthopaedic &amp; Sports<br>Medicine Center</p>
    </div>
  </div>

  <ul class="contact">
    <li class="contact__item">
      <span class="contact__icon"><svg viewBox="0 0 10 10"><path d="M5 0C3 0 1.5 1.5 1.5 3.4 1.5 6 5 10 5 10s3.5-4 3.5-6.6C8.5 1.5 7 0 5 0zm0 4.7a1.3 1.3 0 1 1 0-2.6 1.3 1.3 0 0 1 0 2.6z"/></svg></span>
      2718 Linden Ave., Riverton, LA 70412
    </li>
    <li class="contact__item">
      <span class="contact__icon"><svg viewBox="0 0 10 10"><path d="M2 0.5l1.8 2.2-1 1.2c.6 1.3 1.6 2.3 2.9 2.9l1.2-1L9.5 8 8.3 9.5C4.3 9.2.8 5.7.5 1.7z"/></svg></span>
      (555) 204-7731
    </li>
    <li class="contact__item">
      <span class="contact__icon"><svg viewBox="0 0 10 10"><path d="M0.5 2h9v6h-9zM1.3 2.6L5 5.4l3.7-2.8v-.1H1.3z"/></svg></span>
      gwhitfield@keystoneortho.com
    </li>
  </ul>
</section>

<section class="card card--back">
  <div class="brand">
    <span class="brand__dot"></span>
    <div>
      <p class="brand__name">KEYSTONE</p>
      <p class="brand__sub">Orthopaedic &amp; Sports<br>Medicine Center</p>
    </div>
  </div>
</section>

</body>
</html>
```